Verdant Medispa Business Card

need a business card for our medispa, attached please see the logo.
our website is https://verdantmedispa-example.com

Sorina Belcourt, MD
Internal Medicine

555-204-7193

Sorina@verdantmedispa-example.com

Www.Verdantmedispa-example.com

738 E Harlow Blvd N, Ste 512, Katy, TX 77981

Target Market(s)

MedSpa, Cosmetics, Esthetics

Industry/Entity Type

MedicalSpa

Contact Information for Business Card

Please see the attached business card which i pulled from the internet. I like the idea back as a logo and front with info.

Font styles to use
Decorative

Requirements
Must have
• Color should be matching with Logo and Website theme, Also I like to have QR code for the website

```html
<!DOCTYPE html>
<html lang="en">
<head>
<meta charset="utf-8">
<title>Verdant Medispa Business Card</title>
<link rel="stylesheet" href="https://fonts.googleapis.com/css2?family=Cinzel:wght@700&family=Open+Sans:wght@400;600;700&display=swap">
<style>
  :root {
    --backdrop: #8c6c48;
    --gold: #d4ac3a;
    --gold-light: #e9cf5a;
    --gold-deep: #b8912a;
    --band-light: #f3e06a;
    --ink: #111111;
    --black: #050505;
    --white: #ffffff;
    --cream: #f6ecc8;
  }
  * { box-sizing: border-box; margin: 0; padding: 0; }
  html, body { width: 1200px; height: 746px; overflow: hidden; }
  body {
    background: var(--backdrop);
    font-family: "Open Sans", sans-serif;
    position: relative;
  }
  .card {
    position: absolute;
    top: 224px;
    width: 520px;
    height: 298px;
    border-radius: 34px;
    overflow: hidden;
    box-shadow: 0 6px 18px rgba(0,0,0,0.25);
  }
  .card-front {
    left: 50px;
    background: linear-gradient(135deg, var(--gold-light) 0%, var(--gold) 50%, var(--gold-deep) 100%);
  }
  .card-back {
    left: 630px;
    background: var(--black);
  }
  .band {
    position: absolute;
    left: 0;
    right: 0;
    background: linear-gradient(90deg, var(--gold-deep), var(--band-light) 50%, var(--gold-deep));
  }
  .card-front .band-top { top: 0; height: 12px; }
  .card-front .band-bottom { bottom: 14px; height: 10px; }
  .card-back .band-top { top: 0; height: 16px; }
  .card-back .band-bottom { bottom: 0; height: 14px; }
  .brand {
    position: absolute;
    left: 0;
    right: 0;
    text-align: center;
    font-weight: 400;
    letter-spacing: 1px;
  }
  .card-front .brand { top: 40px; font-size: 26px; color: var(--cream); }
  .card-back .brand { top: 128px; font-size: 38px; color: var(--gold); }
  .identity {
    position: absolute;
    top: 120px;
    right: 272px;
    text-align: right;
  }
  .name {
    font-family: "Cinzel", serif;
    font-weight: 700;
    font-size: 19px;
    line-height: 24px;
    color: var(--ink);
    white-space: nowrap;
  }
  .role {
    font-weight: 700;
    font-size: 12.5px;
    color: var(--cream);
  }
  .divider {
    position: absolute;
    left: 256px;
    top: 118px;
    width: 1px;
    height: 90px;
    background: var(--ink);
  }
  .contact {
    position: absolute;
    left: 266px;
    top: 118px;
    list-style: none;
    font-size: 12px;
    line-height: 17.5px;
    color: var(--white);
    white-space: nowrap;
  }
  .appointment {
    position: absolute;
    left: 24px;
    font-size: 12px;
    color: var(--white);
  }
  .appointment-date { top: 216px; }
  .appointment-time { top: 248px; }
  .leader { letter-spacing: 2px; }
  .qr-code {
    position: absolute;
    right: 30px;
    top: 212px;
    width: 50px;
    height: 50px;
    background: var(--cream);
    border: 3px solid var(--white);
    border-radius: 4px;
  }
</style>
</head>
<body>
  <section class="card card-front" aria-label="Business card front">
    <div class="band band-top"></div>
    <div class="brand">Verdant Medispa</div>
    <div class="identity">
      <div class="name">Sorina Belcourt, MD</div>
      <div class="role">Internal Medicine</div>
    </div>
    <div class="divider"></div>
    <ul class="contact">
      <li>555-204-7193</li>
      <li>Sorina@verdantmedispa-example.com</li>
      <li>Www.Verdantmedispa-example.com</li>
      <li>738 E Harlow Blvd N, Ste 512,</li>
      <li>Katy, TX 77981</li>
    </ul>
    <div class="appointment appointment-date">Date : <span class="leader">.........................</span></div>
    <div class="appointment appointment-time">Time : <span class="leader">.........................</span></div>
    <div class="qr-code" role="img" aria-label="QR code linking to https://verdantmedispa-example.com"></div>
    <div class="band band-bottom"></div>
  </section>

  <section class="card card-back" aria-label="Business card back">
    <div class="band band-top"></div>
    <div class="brand">Verdant Medispa</div>
    <div class="band band-bottom"></div>
  </section>
</body>
</html>
```